11th Annual Vemtora Forum Flyer - Save the Date

We need a flyer for our annual Forum that will be creative with the theme of the Forum while highlighting our conference Title and Topics. Flyer should allow for a header that can be used consistently across conference communication. This is our 11th Annual Forum, which will take place outside of Houston, Texas at Bel Costano Resort and Spa.

Target Market(s)

Architects, engineers, contractors, universities, building project Owners

Industry/Entity Type

Construction

Font styles to use
Sans Serif

Colors

Designer to choose colors to be used in the design.

Requirements
Must have
• Title, date, location, key topics (title only), logo. See attached for breakdown of information.
Nice to have
• Creativity with the theme of the Forum, ability to slice flyer so that a portion can be used for a header in other conference documents.
• Mention of Closing Keynote, Dale Hutton
Should not have
• Please don't use the topic descriptions in the Flyer. Just the main titles of the topics is necessary.
• Should not be too word, but eye-catching with graphics and main

```html
<!DOCTYPE html>
<html lang="en">
<head>
<meta charset="utf-8">
<title>11th Annual Vemtora Forum – Save the Date</title>
<link href="https://fonts.googleapis.com/css2?family=Roboto:wght@400;500;700&family=Rajdhani:wght@500&display=swap" rel="stylesheet">
<style>
  :root{
    --brand-blue:#35509c;
    --brand-green:#8cbc2c;
    --ink-grey:#4a4a4a;
    --box-fill:#f2f2f4;
    --box-line:#9aa6c8;
    --page:#cfcfcf;
    --paper:#ffffff;
  }
  *{box-sizing:border-box;margin:0;padding:0}
  html,body{width:1200px;height:1200px;overflow:hidden}
  body{background:var(--page);font-family:"Roboto",Arial,sans-serif;position:relative}
  .flyer{position:absolute;left:200px;top:35px;width:800px;height:1130px;background:var(--paper);overflow:hidden;text-align:center}
  .flyer__band{position:absolute;left:0;width:800px}
  .flyer__band--top{top:0;height:215px}
  .flyer__band--bottom{bottom:0;height:90px}
  .band-title{position:absolute;top:38px;left:0;width:100%;color:#fff;font-weight:700;font-size:58px;letter-spacing:1px}
  .skyline{position:absolute;top:72px;width:95px;height:110px;background:linear-gradient(#e9edf7,#b9c4e0);opacity:.9}
  .skyline--left{left:0}
  .skyline--right{right:0}
  .backdrop-building{position:absolute;left:120px;top:330px;width:560px;height:520px;background:linear-gradient(#f4f5f9,#fbfbfd);opacity:.7}
  .brand{position:absolute;top:212px;left:0;width:100%;display:flex;justify-content:center;align-items:center;gap:14px}
  .brand__dot{width:68px;height:68px;border-radius:50%;background:var(--brand-blue)}
  .brand__text{text-align:left;color:var(--ink-grey)}
  .brand__name{font-size:38px;font-weight:500;line-height:1}
  .brand__tag{font-size:9px;color:var(--ink-grey);margin-top:4px}
  .year{position:absolute;top:278px;left:0;width:100%;font-family:"Rajdhani",sans-serif;font-weight:500;font-size:178px;line-height:1;color:var(--brand-green);letter-spacing:6px}
  .forum-name{position:absolute;top:420px;left:0;width:100%;font-size:60px;font-weight:500;color:var(--brand-blue)}
  .theme{position:absolute;top:496px;left:86px;width:625px;height:80px;background:var(--brand-blue);border-radius:6px;color:#fff}
  .theme__title{font-size:38px;font-weight:700;margin-top:6px}
  .theme__sub{font-size:19px;font-weight:500;margin-top:-2px}
  .rule-heading{position:absolute;left:0;width:100%;display:flex;align-items:center;justify-content:center;gap:14px;font-weight:500}
  .rule-heading::before,.rule-heading::after{content:"";height:2px;width:100px}
  .rule-heading--green{top:588px;color:var(--brand-green);font-size:38px}
  .rule-heading--green::before,.rule-heading--green::after{background:var(--brand-green)}
  .rule-heading--blue{top:838px;color:var(--brand-blue);font-size:37px}
  .rule-heading--blue::before,.rule-heading--blue::after{background:var(--brand-blue)}
  .topic{position:absolute;top:672px;width:233px;height:153px;background:var(--box-fill);border:2px solid var(--box-line);border-radius:4px}
  .topic--1{left:20px}.topic--2{left:283px}.topic--3{left:547px}
  .topic__num{position:absolute;left:50%;top:-37px;margin-left:-49px;width:98px;height:98px;border-radius:50%;background:var(--brand-blue);border:4px solid #fff;color:#fff;font-size:62px;font-weight:700;line-height:90px}
  .topic__title{position:absolute;top:82px;left:0;width:100%;font-size:22px;color:var(--ink-grey);line-height:1.15;display:flex;align-items:center;justify-content:center;height:52px}
  .highlights{position:absolute;top:892px;left:22px;width:756px;display:flex;justify-content:space-between}
  .pill{width:240px;height:33px;border-radius:6px;background:var(--brand-green);color:#fff;font-weight:700;font-size:14px;line-height:33px}
  .keynote{position:absolute;top:946px;left:0;width:100%;font-size:17px;color:var(--ink-grey)}
  .keynote strong{color:var(--brand-blue)}
  .edition{position:absolute;top:987px;left:106px;width:588px;height:56px;background:var(--brand-blue);border-radius:6px;color:#fff;font-size:48px;font-weight:500;line-height:56px}
  .location{position:absolute;top:1052px;left:0;width:100%;font-size:22px;color:var(--ink-grey)}
</style>
</head>
<body>
<main class="flyer">
  <svg class="flyer__band flyer__band--top" viewBox="0 0 800 215" aria-hidden="true">
    <path d="M0 0H800V210Q400 100 0 205Z" fill="var(--brand-green)"/>
    <path d="M0 0H800V196Q400 88 0 190Z" fill="var(--brand-blue)"/>
  </svg>
  <div class="skyline skyline--left" role="img" aria-label="City skyline of office towers"></div>
  <div class="skyline skyline--right" role="img" aria-label="City skyline of office towers"></div>
  <h1 class="band-title">SAVE THE DATE</h1>

  <div class="backdrop-building" role="img" aria-label="Faint building outline in the background"></div>

  <div class="brand">
    <span class="brand__dot"></span>
    <div class="brand__text">
      <div class="brand__name">I-Vemtora</div>
      <div class="brand__tag">Vemtora Institute for Capital Projects</div>
    </div>
  </div>

  <div class="year">2019</div>
  <h2 class="forum-name">VEMTORA FORUM</h2>

  <div class="theme">
    <div class="theme__title">THE THREE-LEGGED STOOL</div>
    <div class="theme__sub">– BALANCED OR BROKEN?</div>
  </div>

  <h3 class="rule-heading rule-heading--green">THREE KEY TOPICS</h3>

  <div class="topic topic--1"><div class="topic__num">1</div><div class="topic__title">The Right Contract<br>Management</div></div>
  <div class="topic topic--2"><div class="topic__num">2</div><div class="topic__title">The Right Culture</div></div>
  <div class="topic topic--3"><div class="topic__num">3</div><div class="topic__title">The Right<br>Subcontractors</div></div>

  <h3 class="rule-heading rule-heading--blue">PROGRAM HIGHLIGHTS</h3>
  <div class="highlights">
    <div class="pill">THURSDAY: OPENING KEYNOTE</div>
    <div class="pill">LUNCH PRESENTATION</div>
    <div class="pill">FINAL WRAP-UP</div>
  </div>
  <p class="keynote"><strong>FRIDAY:</strong>Closing Keynote, Dale Hutton, author of (among others)</p>

  <div class="edition">11TH ANNUAL FORUM</div>
  <p class="location">outside of Houston, Texas at Bel Costano Resort and Spa</p>

  <svg class="flyer__band flyer__band--bottom" viewBox="0 0 800 90" aria-hidden="true">
    <path d="M0 20Q400 100 800 8V90H0Z" fill="var(--brand-green)"/>
    <path d="M0 34Q400 112 800 22V90H0Z" fill="var(--brand-blue)"/>
  </svg>
</main>
</body>
</html>
```